Velora Aesthetica

Medical doctor providing aesthetic medicine

* Double sided card
* Logo to be on card
Other details:
* Dr. Mirela Kostvan, BSc, MBChB, CCFP
* #214-215, 27903 83 Ave, Surrey, BC, V2T 4K7
* 604-718-2943
* info@veloraclinic.ca
* www.veloraclinic.ca

Industry/Entity Type

Medical / Health & Beauty

Contact Information for Business Card

see 'Project Description'

Colors
0054AA
0677BA
7BADD7
CADEEF
E8F1F8
FFF300
FFF600
FEFA6F
FFFEC7
FFFEE8

Requirements
Must have
• Modern, high-end design

```html
<!DOCTYPE html>
<html lang="en">
<head>
<meta charset="UTF-8">
<title>Velora Aesthetica – Business Card</title>
<link href="https://fonts.googleapis.com/css2?family=Montserrat:wght@400;500;700;800&display=swap" rel="stylesheet">
<style>
  :root {
    --backdrop: #222222;
    --navy: #234264;
    --gold: #d6b02c;
    --white: #ffffff;
    --ink: #1e2a3a;
  }
  * { box-sizing: border-box; margin: 0; padding: 0; }
  html, body { width: 1200px; height: 711px; overflow: hidden; }
  body {
    background: var(--backdrop);
    font-family: "Montserrat", sans-serif;
    display: flex;
    align-items: center;
    justify-content: center;
    gap: 40px;
  }
  .card {
    position: relative;
    width: 540px;
    height: 310px;
    border-radius: 28px;
    overflow: hidden;
  }
  .card--front {
    background: var(--navy);
    display: flex;
    align-items: center;
    justify-content: center;
  }
  .brand {
    display: flex;
    align-items: center;
    gap: 14px;
  }
  .brand__dot {
    width: 18px;
    height: 18px;
    border-radius: 50%;
    background: var(--gold);
  }
  .brand__name {
    font-weight: 500;
    letter-spacing: 0.22em;
    text-transform: uppercase;
  }
  .card--front .brand__name { color: var(--white); font-size: 26px; }
  .card--back { background: var(--white); }
  .card--back .brand {
    position: absolute;
    right: 30px;
    top: 104px;
    gap: 10px;
  }
  .card--back .brand__dot { width: 12px; height: 12px; }
  .card--back .brand__name { color: var(--ink); font-size: 17px; }
  .contact {
    position: absolute;
    left: 34px;
    top: 40px;
    color: var(--ink);
  }
  .contact__name {
    font-size: 19px;
    font-weight: 800;
    color: var(--navy);
    text-transform: uppercase;
    letter-spacing: -0.01em;
  }
  .contact__name span { color: var(--gold); }
  .contact__credentials { font-size: 12.5px; margin-top: 2px; padding-left: 12px; }
  .contact__address { font-size: 12.5px; line-height: 1.4; margin-top: 18px; padding-left: 28px; }
  .contact__list { list-style: none; margin-top: 16px; padding-left: 46px; font-size: 12.5px; line-height: 1.55; }
  .contact__list li { display: flex; align-items: center; gap: 8px; margin-left: -22px; }
  .contact__list svg { width: 14px; height: 14px; fill: var(--gold); flex: none; }
  .wave { position: absolute; left: 0; bottom: 0; width: 540px; height: 310px; }
</style>
</head>
<body>
  <section class="card card--front">
    <div class="brand">
      <span class="brand__dot"></span>
      <span class="brand__name">Velora Aesthetica</span>
    </div>
  </section>

  <section class="card card--back">
    <svg class="wave" viewBox="0 0 540 310" aria-hidden="true">
      <path d="M0 276 C150 246 320 212 540 148 V186 C340 232 170 266 0 304 Z" fill="var(--gold)"/>
      <path d="M0 302 C170 270 350 240 540 190 V310 H0 Z" fill="var(--navy)" stroke="var(--white)" stroke-width="4"/>
    </svg>

    <div class="contact">
      <h1 class="contact__name">Dr. Mirela <span>Kostvan</span></h1>
      <p class="contact__credentials">BSc, MBChB, CCFP</p>
      <p class="contact__address">#214-215, 27903 83 Ave,<br>Surrey, BC, V2T 4K7</p>
      <ul class="contact__list">
        <li>
          <svg viewBox="0 0 24 24"><path d="M6.6 10.8a15 15 0 0 0 6.6 6.6l2.2-2.2a1 1 0 0 1 1-.25 11.4 11.4 0 0 0 3.6.57 1 1 0 0 1 1 1V20a1 1 0 0 1-1 1A17 17 0 0 1 3 4a1 1 0 0 1 1-1h3.5a1 1 0 0 1 1 1c0 1.25.2 2.45.57 3.57a1 1 0 0 1-.25 1z"/></svg>
          604-718-2943
        </li>
        <li>
          <svg viewBox="0 0 24 24"><path d="M2 5h20v14H2z M2 5l10 8 10-8" /></svg>
          info@veloraclinic.ca
        </li>
        <li>
          <svg viewBox="0 0 24 24"><circle cx="12" cy="12" r="10"/></svg>
          www.veloraclinic.ca
        </li>
      </ul>
    </div>

    <div class="brand">
      <span class="brand__dot"></span>
      <span class="brand__name">Velora Aesthetica</span>
    </div>
  </section>
</body>
</html>
```